Dietitian needs awesome business card

I need a contemporary design that's eye catching but professional.
My card is to given to doctors, specialists and patients alike.
I manage patients with chronic diseases
I have uploaded my logo and current business card, I would also like the other Registered Clinical Nutritionist logo incorporated into the design

Target Market(s)

Doctors, specialists and patients

Industry/Entity Type

Healthcare

Contact Information for Business Card

www.brindlecovenutrition.com.au
Ph: 0427 516 903
Fax: 6482 7315
email: marcus.k.wellfare@quorvamail.com
Space on the back of the card with: Appointment date, Appointment time and appointment location

Font styles to use
Serif

Colors
fbee3e
876aae
ffc214

Requirements
Must have
• My Logo
• Registered Clinical Nutritionist Logo
• My 4 locations - Fernhollow Medical Centre, North Kelby Health, Ashcourt Medical, Pinebrook Doctors Surgery
Nice to have
• I like the colours in my current business card

```html
<!DOCTYPE html>
<html lang="en">
<head>
<meta charset="utf-8">
<title>Brindlecove Nutrition &amp; Dietetics – Business Card</title>
<link rel="stylesheet" href="https://fonts.googleapis.com/css2?family=Arimo:wght@400;700&display=swap">
<style>
  :root {
    --page-bg: #e9e9e9;
    --brand-blue: #1b63ad;
    --deep-blue: #0a2a8a;
    --sky-blue: #1a9ee0;
    --leaf-green: #6cb52d;
    --mark-tint: #e7f0dc;
    --mark-tint-back: #f3f7ee;
    --ink: #1a1a1a;
    --rule: #222;
    --badge-orange: #ee7a22;
    --panel: #f2f2f2;
  }
  * { box-sizing: border-box; margin: 0; padding: 0; }
  html, body { width: 1200px; height: 1000px; overflow: hidden; }
  body {
    background: var(--page-bg);
    font-family: "Arimo", Arial, sans-serif;
    color: var(--ink);
    position: relative;
  }
  .card {
    position: absolute;
    width: 665px;
    height: 398px;
    overflow: hidden;
    box-shadow: 0 4px 14px rgba(0,0,0,.25);
  }
  /* ---------- Front ---------- */
  .card-front {
    left: 262px; top: 145px;
    background: linear-gradient(160deg, #ffffff 40%, #ececec 100%);
  }
  .front-swoosh { position: absolute; left: 0; top: 0; width: 665px; height: 150px; }
  .brand-mark {
    position: absolute; border-radius: 50%;
    background: var(--mark-tint);
  }
  .card-front .brand-mark { left: 52px; top: 36px; width: 212px; height: 212px; }
  .brand-name {
    position: absolute; left: 20px; width: 275px; text-align: center;
    color: var(--brand-blue); font-weight: 700; line-height: 1.15;
  }
  .card-front .brand-name { top: 266px; font-size: 27px; }
  .card-front .brand-name span { display: block; font-size: 17px; }
  .accreditation {
    position: absolute; left: 55px; top: 342px;
    display: flex; align-items: center; gap: 8px;
    font-size: 10px; font-weight: 700; line-height: 1.15;
  }
  .accreditation-badge { width: 80px; height: 38px; background: var(--badge-orange); }
  .divider { position: absolute; left: 330px; top: 113px; width: 2px; height: 253px; background: var(--leaf-green); }
  .person-name { position: absolute; left: 340px; top: 112px; font-size: 26px; letter-spacing: .5px; }
  .person-name small { font-size: 19px; }
  .person-role { position: absolute; left: 342px; top: 143px; font-size: 17px; color: var(--brand-blue); }
  .contact-list {
    position: absolute; left: 352px; top: 184px; list-style: none;
    font-size: 13px;
  }
  .contact-list li { display: flex; align-items: center; height: 20.5px; }
  .contact-list svg { width: 13px; height: 13px; margin-right: 18px; flex: none; }
  .contact-list b { font-weight: 400; font-size: 16px; margin-right: 4px; }
  .locations {
    position: absolute; left: 348px; top: 282px; width: 320px; height: 85px;
    border: 2px solid var(--leaf-green); border-right: none;
    display: flex; padding: 9px 0 0 8px; font-size: 14px;
  }
  .locations h2 { font-size: 14px; font-weight: 400; width: 110px; }
  .locations ul { list-style: none; color: var(--brand-blue); font-size: 12.5px; line-height: 13px; }
  .locations li:last-child { margin-top: 4px; }
  /* ---------- Back ---------- */
  .card-back {
    left: 267px; top: 557px; height: 401px;
    background: radial-gradient(ellipse 55% 60% at 50% 40%, var(--sky-blue) 0%, #1360c4 45%, var(--deep-blue) 100%);
  }
  .card-back .brand-mark {
    left: 264px; top: 12px; width: 136px; height: 136px;
    background: var(--mark-tint-back);
  }
  .card-back .brand-name { left: 192px; width: 280px; top: 160px; font-size: 19px; color: #ffffff; }
  .card-back .brand-name span { display: block; font-size: 11.5px; }
  .appointment-panel {
    position: absolute; left: 14px; top: 205px; width: 634px; height: 176px;
    background: var(--panel); text-align: center;
  }
  .appointment-title {
    width: 398px; margin: 36px auto 0; border-top: 2px solid var(--rule);
    font-size: 21px; font-weight: 400; padding-top: 5px;
  }
  .weekday-row {
    display: flex; justify-content: center; gap: 10px; margin-top: 10px; font-size: 16px;
  }
  .weekday-row span { display: flex; align-items: flex-start; gap: 4px; }
  .weekday-row i { width: 19px; height: 19px; border: 1px solid #777; display: inline-block; margin-top: -4px; }
  .schedule-row { display: flex; justify-content: center; gap: 26px; margin-top: 24px; font-size: 17px; }
  .schedule-row span { display: flex; align-items: flex-end; gap: 6px; }
  .schedule-row i { display: inline-block; width: 140px; border-bottom: 2px solid var(--rule); margin-bottom: 3px; }
  .schedule-row span:last-child i { width: 108px; }
  .notice { font-size: 12px; margin-top: 6px; letter-spacing: -.2px; }
</style>
</head>
<body>

<section class="card card-front" aria-label="Business card front">
  <svg class="front-swoosh" viewBox="0 0 665 150" aria-hidden="true">
    <defs>
      <linearGradient id="swoosh-blue" x1="0" y1="0" x2="1" y2="0">
        <stop offset="0" stop-color="#7c97cf"/><stop offset="1" stop-color="#2b3f9c"/>
      </linearGradient>
      <linearGradient id="swoosh-green" x1="0" y1="0" x2="1" y2="0">
        <stop offset="0" stop-color="#cfe6a0"/><stop offset=".5" stop-color="#9ccc2c"/><stop offset="1" stop-color="#6cb52d"/>
      </linearGradient>
    </defs>
    <path d="M250 0 H665 V112 C560 55 420 18 250 0 Z" fill="url(#swoosh-blue)"/>
    <path d="M0 4 C260 2 500 40 665 118 V134 C480 58 270 14 0 12 Z" fill="url(#swoosh-green)"/>
  </svg>

  <div class="brand-mark" aria-hidden="true"></div>
  <p class="brand-name">BRINDLECOVE<span>Nutrition &amp; Dietetics</span></p>

  <div class="accreditation">
    <div class="accreditation-badge" role="img" aria-label="Registered Clinical Nutritionist badge"></div>
    <p>ACCREDITED<br>&amp;<br>RECOGNIZED BY:</p>
  </div>

  <div class="divider"></div>
  <h1 class="person-name">MARCUS <small>KELLWAY</small></h1>
  <p class="person-role">Dietician/ Nutritionist/ Chef</p>

  <ul class="contact-list">
    <li><svg viewBox="0 0 16 16"><path d="M2 5c0-2 2-3 6-3s6 1 6 3v1h-3V5H5v1H2z M4 8h8l2 5H2z" fill="#333"/></svg><b>PH:</b> 0427 516 903</li>
    <li><svg viewBox="0 0 16 16"><rect x="2" y="5" width="12" height="9" fill="#333"/><rect x="4" y="1" width="8" height="5" fill="#fff" stroke="#333"/></svg><b>FAX:</b> 0427 516 903</li>
    <li><svg viewBox="0 0 16 16"><text x="8" y="13" font-size="14" text-anchor="middle" fill="#333" font-family="Arial">@</text></svg><b>EMAIL:</b> marcus.k.wellfare@quorvamail.com</li>
    <li><svg viewBox="0 0 16 16"><circle cx="8" cy="8" r="6.5" fill="none" stroke="#666"/><path d="M1.5 8h13M8 1.5v13M3 4.5h10M3 11.5h10" stroke="#666" fill="none"/></svg><b>WEB:</b> www.brindlecovenutrition.com.au</li>
  </ul>

  <div class="locations">
    <h2>Find Me Here</h2>
    <ul>
      <li>- Fernhollow Medical Centre</li>
      <li>- North Kelby Health</li>
      <li>- Ashcourt Medical</li>
      <li>- Pinebrook Doctors Surgery</li>
    </ul>
  </div>
</section>

<section class="card card-back" aria-label="Business card back">
  <div class="brand-mark" aria-hidden="true"></div>
  <p class="brand-name">BRINDLECOVE<span>Nutrition &amp; Dietetics</span></p>

  <div class="appointment-panel">
    <h2 class="appointment-title">Has An Appointment ;</h2>
    <div class="weekday-row">
      <span>Mon <i></i></span><span>Tue <i></i></span><span>Wed<i></i></span>
      <span>Thr <i></i></span><span>Fri <i></i></span><span>Sat <i></i></span>
    </div>
    <div class="schedule-row">
      <span>Date <i></i></span><span>Time <i></i></span>
    </div>
    <p class="notice">If unavailable kindly notify us 24 hours, in advance for reschedule.</p>
  </div>
</section>

</body>
</html>
```